Window and GutterCleaning Flyer A5 size double sided.

We need a double sided A5 flyer. Side 1, is for window cleaning, side 2 is for gutter cleaning. Licensed by Borough of Calderwick Authority.
Phone number 0800 471 3926.
Business address 17 Fenmarrow Loan, West Brankholm Edinburgh EH47 3TP.
www.bright-pane-services.example
We use a LoftOrb Gutter inspection Cam to view your gutters first to see if they need doing.
Window cleaning ; Professional window cleaning services, what we offer, water fed pole window cleaning able to reach windows up to 60 feet.
Conservatory cleaning.
Conservatory roof cleaning.
Fascias & Soffits cleaning.
Excellent Customer Service.
Target Market(s)
domestic houses
Industry/Entity Type
window cleaning
Look and feel
Each slider illustrates characteristics of the customer's brand and the style your logo design should communicate.

```html
<!DOCTYPE html>
<html lang="en">
<head>
<meta charset="utf-8">
<title>Bright Pane Services – Window &amp; Gutter Cleaning Flyer</title>
<link rel="stylesheet" href="https://fonts.googleapis.com/css2?family=Barlow:wght@500;600;700;800&family=Barlow+Semi+Condensed:wght@500;700&family=Jost:wght@400;500&display=swap">
<style>
  :root {
    --stage: #a3a3a3;
    --navy: #24225f;
    --blue: #1f6cc6;
    --blue-deep: #1750a8;
    --blue-mid: #2f86da;
    --sky: #6cc0ee;
    --pale: #dbeaf8;
    --white: #ffffff;
    --gold: #e0a92a;
  }
  * { box-sizing: border-box; margin: 0; padding: 0; }
  html, body { width: 1200px; height: 826px; overflow: hidden; background: var(--stage); }
  body { position: relative; font-family: "Barlow", sans-serif; }

  .flyer {
    position: absolute; top: 53px; width: 508px; height: 720px; overflow: hidden;
    background: linear-gradient(160deg, #f4f9fe 0%, #cfe4f7 32%, #5ea6e6 62%, #2a74cf 100%);
  }
  .flyer--window { left: 64px; }
  .flyer--gutter { left: 620px; width: 509px; height: 721px; }

  .abs { position: absolute; }
  .photo { position: absolute; }

  .brand {
    position: absolute; left: 40px; top: 52px; width: 150px; text-align: center;
    font-family: "Barlow", sans-serif; font-weight: 800; color: var(--navy);
    font-size: 24px; line-height: 1.05; text-transform: uppercase;
  }

  .title-pro { position: absolute; left: 51px; top: 166px; font-size: 26px; font-weight: 800; color: var(--navy); }
  .title-main { position: absolute; left: 29px; top: 188px; font-size: 62px; font-weight: 800; color: var(--navy); letter-spacing: -1px; line-height: 1; }
  .title-sub { position: absolute; left: 54px; top: 246px; font-size: 44px; font-weight: 800; color: var(--blue); line-height: 1; }
  .flyer--gutter .title-main { left: 68px; }
  .flyer--gutter .title-sub { left: 54px; }

  .offer-heading { position: absolute; left: 47px; top: 322px; font-size: 28px; font-weight: 500; color: var(--navy); white-space: nowrap; }
  .offer-heading b { font-weight: 800; }

  .pill {
    position: absolute; height: 29px; border-radius: 7px;
    background: var(--pale); display: flex; align-items: center; gap: 6px; padding-left: 10px;
    font-family: "Barlow Semi Condensed", sans-serif; font-size: 18px; font-weight: 700; color: var(--navy);
    white-space: nowrap;
  }
  .pill svg { width: 16px; height: 16px; flex: none; }

  .side-panel { position: absolute; left: 364px; top: 467px; width: 144px; height: 253px; background: var(--sky); }
  .side-text { position: absolute; left: 386px; font-family: "Jost", sans-serif; font-size: 13px; line-height: 15.6px; color: var(--white); width: 116px; }
  .reach-pill {
    position: absolute; left: 384px; top: 679px; width: 98px; height: 18px; border-radius: 9px;
    background: var(--blue-deep); color: var(--white); font-weight: 700; font-size: 12px;
    display: flex; align-items: center; justify-content: center; white-space: nowrap;
  }

  .contact { position: absolute; left: 36px; color: var(--white); white-space: nowrap; }
  .contact .address { font-size: 11.5px; font-weight: 500; }
  .contact .phone { display: flex; align-items: center; gap: 4px; font-size: 25px; font-weight: 700; line-height: 1.1; margin-top: 2px; }
  .contact .phone svg { width: 14px; height: 16px; }
  .contact .web { font-size: 13px; font-weight: 500; color: #a9d3f5; }

  .intro { position: absolute; left: 49px; top: 321px; width: 196px; font-size: 11.6px; font-weight: 700; line-height: 12.2px; color: var(--white); }
  .info-text { position: absolute; left: 270px; width: 224px; font-family: "Jost", sans-serif; font-size: 10.6px; line-height: 12.1px; color: var(--white); }

  .card { position: absolute; top: 459px; width: 98px; height: 131px; border-radius: 9px; background: var(--blue-deep); overflow: hidden; border: 1.5px solid #cfe3f7; }
  .card .card-photo { height: 100px; border-radius: 0 0 8px 8px; }
  .card .card-label { padding: 4px 0 0 12px; font-size: 9.6px; font-weight: 700; color: var(--white); line-height: 9.6px; white-space: nowrap; }

  .guarantee-text { position: absolute; left: 368px; top: 624px; width: 128px; font-size: 10.8px; font-weight: 700; line-height: 12px; color: var(--white); }
</style>
</head>
<body>

<!-- Side 1: window cleaning -->
<section class="flyer flyer--window">
  <div class="photo" role="img" aria-label="Window cleaner wiping a tall glass window with a cloth" style="left:246px;top:0;width:262px;height:310px;background:radial-gradient(ellipse at 60% 40%, #c5a896 0%, #9a7b6e 18%, #d9e4ee 45%, rgba(220,234,247,0) 75%);"></div>
  <div class="photo" role="img" aria-label="Gutter inspection camera screen on a pole" style="left:340px;top:286px;width:142px;height:181px;border-radius:14px;background:linear-gradient(160deg,#3a3a3a,#1f2a36 60%,#e07a1f 100%);opacity:.9;"></div>

  <svg class="abs" style="left:0;top:0" width="508" height="720" aria-hidden="true">
    <path d="M0 720 V615 H300 C330 615 345 650 345 700 V720 Z" fill="var(--blue-deep)"/>
    <path d="M300 612 C334 612 352 650 352 720" fill="none" stroke="#cfe3f7" stroke-width="1"/>
  </svg>

  <div class="photo" role="img" aria-label="White conservatory with brick base" style="left:0;top:470px;width:91px;height:186px;border-radius:0 60px 60px 0;background:linear-gradient(180deg,#9fc6ea 0%,#eef3f7 45%,#b36a4a 100%);"></div>
  <div class="photo" role="img" aria-label="Inspection camera tablet showing a house" style="left:195px;top:532px;width:126px;height:99px;border-radius:12px;transform:rotate(-12deg);background:linear-gradient(150deg,#2c2c2c,#34506a 55%,#e07a1f);"></div>

  <div class="side-panel"></div>

  <div class="brand">Bright Pane Services</div>

  <div class="title-pro">Professional</div>
  <div class="title-main">Window</div>
  <div class="title-sub">Cleaning</div>

  <div class="offer-heading">What <b>we offer</b></div>

  <div class="pill" style="left:50px;top:368px;width:238px;"><svg viewBox="0 0 16 16"><circle cx="8" cy="8" r="8" fill="var(--blue-mid)"/><path d="M4.5 8.3l2.3 2.3 4.7-4.9" fill="none" stroke="#fff" stroke-width="1.8"/></svg>Conservatory cleaning</div>
  <div class="pill" style="left:79px;top:405px;width:250px;"><svg viewBox="0 0 16 16"><circle cx="8" cy="8" r="8" fill="var(--blue-mid)"/><path d="M4.5 8.3l2.3 2.3 4.7-4.9" fill="none" stroke="#fff" stroke-width="1.8"/></svg>Conservatory roof cleaning</div>
  <div class="pill" style="left:50px;top:443px;width:238px;"><svg viewBox="0 0 16 16"><circle cx="8" cy="8" r="8" fill="var(--blue-mid)"/><path d="M4.5 8.3l2.3 2.3 4.7-4.9" fill="none" stroke="#fff" stroke-width="1.8"/></svg>Fascias &amp; Soffits cleaning</div>
  <div class="pill" style="left:79px;top:480px;width:255px;"><svg viewBox="0 0 16 16"><circle cx="8" cy="8" r="8" fill="var(--blue-mid)"/><path d="M4.5 8.3l2.3 2.3 4.7-4.9" fill="none" stroke="#fff" stroke-width="1.8"/></svg>Excellent Customer Service</div>

  <p class="side-text" style="top:486px;">We use a LoftOrb Gutter inspection Cam to view your gutters first to see if they need doing.</p>
  <p class="side-text" style="top:612px;">Water fed pole window cleaning able to reach windows</p>
  <div class="reach-pill">up to 60 feet</div>

  <div class="contact" style="top:643px;">
    <div class="address">17 Fenmarrow Loan, West Brankholm Edinburgh EH47 3TP</div>
    <div class="phone"><svg viewBox="0 0 14 16"><path d="M3 1l3 3-2 2c1 2 3 4 5 5l2-2 3 3-2 3C6 15 0 8 1 3z" fill="#cfe3f7"/></svg>0800 471 3926</div>
    <div class="web">www.bright-pane-services.example</div>
  </div>
</section>

<!-- Side 2: gutter cleaning -->
<section class="flyer flyer--gutter">
  <div class="photo" role="img" aria-label="Gloved hand lifting autumn leaves out of a house gutter" style="left:209px;top:0;width:300px;height:230px;background:radial-gradient(ellipse at 65% 35%, #c9762a 0%, #a9936a 22%, #d7dee6 48%, rgba(220,234,247,0) 78%);"></div>

  <svg class="abs" style="left:0;top:0" width="509" height="721" aria-hidden="true">
    <path d="M0 721 V612 H290 C322 612 343 650 343 700 V721 Z" fill="var(--blue-deep)"/>
    <path d="M290 610 C330 610 350 650 350 721" fill="none" stroke="#cfe3f7" stroke-width="1"/>
    <circle cx="313" cy="227" r="42" fill="var(--gold)"/>
    <circle cx="313" cy="227" r="30" fill="#fdf6e4"/>
  </svg>

  <div class="brand">Bright Pane Services</div>

  <div class="title-pro">Professional</div>
  <div class="title-main">Gutter</div>
  <div class="title-sub">Cleaning</div>

  <p class="intro">Bright Pane Services offer a fast and easy gutter cleaning service on residential and commercial properties.</p>

  <p class="info-text" style="top:290px;">Gutters are an important part of your home. Letting your gutters get blocked up can cause damage to your property, so why not set up an annual plan and make sure you don’t run into problems when winter comes.</p>
  <p class="info-text" style="top:363px;">Over time your gutters will fill up with moss, leaves and other unwanted debris which will affect the appearance of your home. When gutters aren’t cleared and emptied on a regular basis they become heavy and risk pulling away from the fascias.</p>

  <div class="offer-heading" style="top:413px;">What <b>we offer</b></div>

  <div class="card" style="left:47px;">
    <div class="card-photo" role="img" aria-label="Vacuum hose cleaning a gutter" style="background:linear-gradient(160deg,#6f8a5a,#2c4fb0 50%,#d9d6d0);"></div>
    <div class="card-label" style="padding-top:8px;">Gutter cleaning</div>
  </div>
  <div class="card" style="left:154px;">
    <div class="card-photo" role="img" aria-label="Mossy conservatory roof panels" style="background:linear-gradient(170deg,#b9a98a,#8f8a5c 50%,#d6dcd8);"></div>
    <div class="card-label">Conservatory roof<br>cleaning</div>
  </div>
  <div class="card" style="left:262px;">
    <div class="card-photo" role="img" aria-label="Roof edge showing gutter, fascia and soffit" style="background:linear-gradient(160deg,#f2f4f6,#c9d2da 60%,#8a5a48);"></div>
    <div class="card-label">Fascias &amp; Soffits<br>cleaning</div>
  </div>
  <div class="card" style="left:370px;">
    <div class="card-photo" role="img" aria-label="Customer service agent wearing a headset" style="background:linear-gradient(160deg,#e9eef3,#d8c2ad 55%,#c9d6e2);"></div>
    <div class="card-label">Excellent<br>Customer Service</div>
  </div>

  <div class="contact" style="top:646px;">
    <div class="address">17 Fenmarrow Loan, West Brankholm Edinburgh EH47 3TP</div>
    <div class="phone"><svg viewBox="0 0 14 16"><path d="M3 1l3 3-2 2c1 2 3 4 5 5l2-2 3 3-2 3C6 15 0 8 1 3z" fill="#cfe3f7"/></svg>0800 471 3926</div>
    <div class="web">www.bright-pane-services.example</div>
  </div>

  <p class="guarantee-text">All our services comes with a 100% satisfaction guarantee. If you’re not happy, we’ll come back and do it again for no additional cost.</p>
</section>

</body>
</html>
```